Business Card, Stationary, and Invoice
PuzzleHarbor
Business Card, Stationary, and Invoice - Games
Creative Brief
Use specific fonts
Use logo font..or similar if logo font doesn't look good.
Bright & Fun-filled
Lyle Ostrand
Owner
84 Brackett Lane Fernhollow, OR 97499
lyle@puzzleharbor-example.com
www.puzzleharbor-example.com
Require business card, stationary, and invoice.

```html
<!DOCTYPE html>
<html lang="en">
<head>
<meta charset="utf-8">
<title>PuzzleHarbor – Business Card</title>
<link rel="stylesheet" href="https://fonts.googleapis.com/css2?family=Source+Sans+3:wght@400;600;700;900&display=swap">
<style>
  :root {
    --backdrop: #ece8e1;
    --card-white: #ffffff;
    --gold-light: #c9ab72;
    --gold: #a88a52;
    --gold-dark: #7e6636;
    --ink: #2b2519;
    --ink-soft: #4a4336;
    --rule: #cfc6b4;
  }
  * { box-sizing: border-box; margin: 0; padding: 0; }
  html, body { width: 1200px; height: 780px; overflow: hidden; }
  body {
    background: var(--backdrop);
    font-family: "Source Sans 3", "Helvetica Neue", Arial, sans-serif;
    color: var(--ink);
    position: relative;
  }
  .business-card {
    position: absolute;
    left: 75px; top: 90px;
    width: 1050px; height: 600px;
    background: var(--card-white);
    border-radius: 34px;
    overflow: hidden;
    box-shadow: 0 6px 24px rgba(60, 45, 20, 0.18);
  }
  .top-band {
    position: absolute;
    left: 0; top: 0;
    width: 100%; height: 160px;
    background: linear-gradient(180deg, var(--gold-light) 0%, var(--gold) 60%, var(--gold-dark) 100%);
  }
  .brand {
    position: absolute;
    left: 250px; top: 105px;
    display: flex; align-items: center; gap: 20px;
  }
  .brand-circle {
    width: 110px; height: 110px;
    border-radius: 50%;
    background: radial-gradient(circle at 40% 35%, #efe0bb 0%, var(--gold-light) 55%, var(--gold) 100%);
  }
  .brand-name {
    font-weight: 900;
    font-size: 60px;
    letter-spacing: -1px;
    color: var(--ink);
    line-height: 1;
  }
  .identity {
    position: absolute;
    right: 550px; top: 310px;
    text-align: right;
    line-height: 1.2;
  }
  .identity .person-name { font-weight: 700; font-size: 30px; color: var(--ink); }
  .identity .person-role { font-size: 23px; color: var(--ink-soft); margin-bottom: 22px; }
  .identity .address { font-weight: 600; font-size: 25px; color: var(--ink); }
  .divider {
    position: absolute;
    left: 528px; top: 300px;
    width: 2px; height: 175px;
    background: var(--rule);
  }
  .contact-list {
    position: absolute;
    left: 556px; top: 300px;
    list-style: none;
  }
  .contact-list li {
    display: flex; align-items: center; gap: 16px;
    font-size: 24px; color: var(--ink-soft);
    height: 52px;
  }
  .contact-list svg { width: 26px; height: 26px; flex: none; }
</style>
</head>
<body>
  <div class="business-card">
    <div class="top-band"></div>

    <div class="brand">
      <div class="brand-circle"></div>
      <span class="brand-name">PuzzleHarbor</span>
    </div>

    <div class="identity">
      <p class="person-name">Lyle Ostrand</p>
      <p class="person-role">Owner</p>
      <p class="address">84 Brackett Lane<br>Fernhollow, OR 97499</p>
    </div>

    <div class="divider"></div>

    <ul class="contact-list">
      <li>
        <svg viewBox="0 0 24 24" aria-hidden="true">
          <rect x="6" y="2" width="12" height="20" rx="2.5" fill="none" stroke="#a88a52" stroke-width="2"/>
          <rect x="9" y="5" width="6" height="8" fill="#c9ab72"/>
          <circle cx="12" cy="18" r="1.4" fill="#a88a52"/>
        </svg>
        <span>555-301-0142</span>
      </li>
      <li>
        <svg viewBox="0 0 24 24" aria-hidden="true">
          <circle cx="12" cy="12" r="4" fill="none" stroke="#a88a52" stroke-width="2"/>
          <path d="M16 8v5.5a2.5 2.5 0 0 0 5 0V12a9 9 0 1 0-3.5 7.1" fill="none" stroke="#a88a52" stroke-width="2" stroke-linecap="round"/>
        </svg>
        <span>lyle@puzzleharbor-example.com</span>
      </li>
      <li>
        <svg viewBox="0 0 24 24" aria-hidden="true">
          <circle cx="12" cy="12" r="9.5" fill="none" stroke="#a88a52" stroke-width="2"/>
          <ellipse cx="12" cy="12" rx="4" ry="9.5" fill="none" stroke="#a88a52" stroke-width="1.6"/>
          <line x1="2.5" y1="12" x2="21.5" y2="12" stroke="#a88a52" stroke-width="1.6"/>
        </svg>
        <span>www.puzzleharbor-example.com</span>
      </li>
    </ul>
  </div>
</body>
</html>
```